Leading In-Home Tutoring Company Needs Web Banners

We need a suite of web banners for our re-marketing campaign. We are based in Melbourne and heading into the busiest time of the year with back to school and we would like to help guide parents to working with us via quality designed banners with the right CTAs. Banner specs as follows (W x H in pixels)
Medium Rectangle: 300 x 250
Vertical rectangle: 240 x 400
Banner: 468 x 60
Leaderboard: 728 x 90
Square: 250 x 250
Mobile leaderboard: 320 x 50
Updates

Hi designers I'm new to this and didn't realise that I had to upload all files at the beginning. I have images that can be used for this project. Just need to work out how to upload them. Added Sunday, January 22, 2017

Hi awesome designers... I've updated the brief now with new files :)

Target Market(s)

Mothers who value kids education. Our customer can be found having morning coffee with friends in her lycra as she prepares to go to the gym. Middle class, inner city and suburban Mums. Most likely on Friendnook.

Industry/Entity Type

It Company

Font styles to use
Sans Serif

Colors
0692cd
fbed22
f47f39
ec1f27

Requirements
Must have
• Wording should include.
• What we do: 1:1, In-Home Tutoring
• Value proposition: The Best Tutor For Your Child
• Call to Action - Free Assessment > Find Out More
• Adjusted layout to suit the sizes. Use of image where possible to provide immediate graphic display of what we do
Nice to have
• Keep it simple, create an emotive connection. Kids matter to parents and they will pay for services if we can create banners that show we care and can help wtih their education.
Should not have
• Anything negative or use fear marketing

```html
<!DOCTYPE html>
<html lang="en">
<head>
<meta charset="utf-8">
<title>StudyNest Web Banner Suite</title>
<link rel="stylesheet" href="https://fonts.googleapis.com/css2?family=Oswald:wght@400;500&display=swap">
<style>
  :root{
    --blue:#0692cd;
    --steel:#3f86bb;
    --orange:#f47f39;
    --orange-light:#f9a04a;
    --red:#ec1f27;
    --ink:#1c1c1c;
    --pill:#ececec;
    --paper:#ffffff;
    --mist:#e9e9e9;
    --photo-a:#9aa9c4;
    --photo-b:#dfe3ea;
  }
  html,body{margin:0;padding:0;overflow:hidden}
  body{
    width:1200px;height:1200px;
    background:radial-gradient(ellipse at 50% 45%, #ffffff 0%, #eeeeee 55%, #d9d9d9 100%);
    font-family:"Oswald", "Arial Narrow", sans-serif;
    position:relative;
  }
  .banner{
    position:absolute;overflow:hidden;
    box-shadow:0 3px 6px rgba(0,0,0,.25);
  }
  .banner svg.art{position:absolute;inset:0;width:100%;height:100%}
  .brand{
    position:absolute;color:var(--steel);font-weight:500;white-space:nowrap;
    display:flex;align-items:center;gap:.25em;
  }
  .brand .dot{width:.45em;height:.45em;border-radius:50%;background:var(--orange)}
  .headline{position:absolute;color:var(--paper);font-weight:400;white-space:nowrap;text-align:center;transform:translateX(-50%)}
  .cta{
    position:absolute;transform:translateX(-50%);white-space:nowrap;
    background:var(--pill);color:var(--ink);border-radius:999px;
    padding:.25em .9em;font-weight:400;box-shadow:0 1px 2px rgba(0,0,0,.25);
  }
  .service{position:absolute;color:var(--paper);white-space:nowrap;transform:translateX(-50%)}

  /* square formats */
  .square .brand{left:7%;top:17%;font-size:.085em}
  .square .headline{left:52%;top:52%;font-size:.085em}
  .square .cta{left:52%;top:66%;font-size:.052em}
  .square .service{left:52%;top:78.5%;font-size:.09em}

  /* horizontal formats */
  .strip .brand{left:3.5%;top:44%;font-size:.19em}
  .strip .divider{position:absolute;left:23.6%;top:22%;height:62%;width:1px;background:#b8b8b8}
  .strip .offer{position:absolute;left:25%;top:13%;line-height:1}
  .strip .offer .ratio{display:block;color:var(--ink);font-size:.22em}
  .strip .offer .kind{display:block;color:var(--red);font-size:.32em;margin-top:.04em}
  .strip .headline{left:63%;top:12%;font-size:.27em}
  .strip .cta{left:63%;top:52%;font-size:.17em}
</style>
</head>
<body>

<!-- Medium rectangle -->
<div class="banner square" style="left:141px;top:267px;width:322px;height:268px;font-size:268px">
  <svg class="art" viewBox="0 0 100 100" preserveAspectRatio="none">
    <defs>
      <linearGradient id="og1" x1="0" y1="0" x2="0" y2="1"><stop offset="0" stop-color="#f9a24d"/><stop offset="1" stop-color="#f37a30"/></linearGradient>
      <linearGradient id="ph1" x1="0" y1="0" x2="1" y2="1"><stop offset="0" stop-color="var(--photo-a)"/><stop offset="1" stop-color="var(--photo-b)"/></linearGradient>
    </defs>
    <rect width="100" height="100" fill="#fff"/>
    <g role="img" aria-label="Tutor and student working together at a desk in front of a bookshelf">
      <polygon points="62,0 100,0 100,32 57,42" fill="url(#ph1)"/>
    </g>
    <polygon points="60,0 62,0 57,42 55,42" fill="var(--steel)"/>
    <path d="M0,41 C20,34 40,46 60,43 C80,40 90,35 100,29 L100,35 C90,41 80,46 60,48 C40,50 20,42 0,47Z" fill="var(--steel)"/>
    <path d="M0,47 C20,42 40,50 60,48 C80,46 90,41 100,35 L100,95 L0,95Z" fill="url(#og1)"/>
    <rect y="95" width="100" height="5" fill="var(--steel)"/>
  </svg>
  <div class="brand">StudyNest<span class="dot"></span></div>
  <div class="headline">The Best Tutor For Your Child</div>
  <div class="cta">Free Assessment - Find Out More</div>
  <div class="service">1:1 IN-HOME TUTORING</div>
</div>

<!-- Square -->
<div class="banner square" style="left:492px;top:309px;width:273px;height:227px;font-size:227px">
  <svg class="art" viewBox="0 0 100 100" preserveAspectRatio="none">
    <defs>
      <linearGradient id="og2" x1="0" y1="0" x2="0" y2="1"><stop offset="0" stop-color="#f9a24d"/><stop offset="1" stop-color="#f37a30"/></linearGradient>
      <linearGradient id="ph2" x1="0" y1="0" x2="1" y2="1"><stop offset="0" stop-color="var(--photo-a)"/><stop offset="1" stop-color="var(--photo-b)"/></linearGradient>
    </defs>
    <rect width="100" height="100" fill="#fff"/>
    <g role="img" aria-label="Tutor and student working together at a desk in front of a bookshelf">
      <polygon points="63,0 100,0 100,30 58,42" fill="url(#ph2)"/>
    </g>
    <polygon points="61,0 63,0 58,42 56,42" fill="var(--steel)"/>
    <path d="M0,39 C20,33 40,45 60,42 C80,39 90,34 100,28 L100,34 C90,40 80,45 60,47 C40,49 20,41 0,46Z" fill="var(--steel)"/>
    <path d="M0,46 C20,41 40,49 60,47 C80,45 90,40 100,34 L100,96 L0,96Z" fill="url(#og2)"/>
    <rect y="96" width="100" height="4" fill="var(--steel)"/>
  </svg>
  <div class="brand">StudyNest<span class="dot"></span></div>
  <div class="headline" style="top:54%">The Best Tutor For Your Child</div>
  <div class="cta" style="top:67%">Free Assessment - Find Out More</div>
  <div class="service" style="top:80%">1:1 IN-HOME TUTORING</div>
</div>

<!-- Three horizontal strips share one layout -->
<div class="banner strip" style="left:141px;top:570px;width:635px;height:79px;font-size:79px">
  <svg class="art" viewBox="0 0 100 100" preserveAspectRatio="none">
    <defs>
      <linearGradient id="gs1" x1="0" y1="0" x2="1" y2="0"><stop offset="0" stop-color="#e4e4e4"/><stop offset=".5" stop-color="#fff"/><stop offset="1" stop-color="#e8e8e8"/></linearGradient>
      <linearGradient id="os1" x1="0" y1="0" x2="0" y2="1"><stop offset="0" stop-color="#f9a24d"/><stop offset="1" stop-color="#f37a30"/></linearGradient>
      <linearGradient id="ps1" x1="0" y1="0" x2="1" y2="1"><stop offset="0" stop-color="var(--photo-a)"/><stop offset="1" stop-color="var(--photo-b)"/></linearGradient>
    </defs>
    <rect width="100" height="100" fill="url(#gs1)"/>
    <path d="M0,0 L6,0 C2.5,25 1,60 1,100 L0,100Z" fill="var(--blue)"/>
    <polygon points="38.5,0 40.8,0 47,100 44.8,100" fill="var(--steel)"/>
    <polygon points="40.8,0 84,0 79,100 47,100" fill="url(#os1)"/>
    <polygon points="84,0 85,0 80,100 79,100" fill="#f3e2c8"/>
    <g role="img" aria-label="Tutor and student working together at a desk in front of a bookshelf">
      <polygon points="85,0 100,0 100,100 80,100" fill="url(#ps1)"/>
    </g>
  </svg>
  <div class="brand">StudyNest<span class="dot"></span></div>
  <div class="divider"></div>
  <div class="offer"><span class="ratio">1:1 IN-HOME</span><span class="kind">TUTORING</span></div>
  <div class="headline">The Best Tutor For Your Child</div>
  <div class="cta">Free Assessment - Find Out More</div>
</div>

<div class="banner strip" style="left:141px;top:700px;width:783px;height:97px;font-size:97px">
  <svg class="art" viewBox="0 0 100 100" preserveAspectRatio="none">
    <defs>
      <linearGradient id="gs2" x1="0" y1="0" x2="1" y2="0"><stop offset="0" stop-color="#e4e4e4"/><stop offset=".5" stop-color="#fff"/><stop offset="1" stop-color="#e8e8e8"/></linearGradient>
      <linearGradient id="os2" x1="0" y1="0" x2="0" y2="1"><stop offset="0" stop-color="#f9a24d"/><stop offset="1" stop-color="#f37a30"/></linearGradient>
      <linearGradient id="ps2" x1="0" y1="0" x2="1" y2="1"><stop offset="0" stop-color="var(--photo-a)"/><stop offset="1" stop-color="var(--photo-b)"/></linearGradient>
    </defs>
    <rect width="100" height="100" fill="url(#gs2)"/>
    <path d="M0,0 L6,0 C2.5,25 1,60 1,100 L0,100Z" fill="var(--blue)"/>
    <polygon points="39,0 41,0 47.5,100 45.5,100" fill="var(--steel)"/>
    <polygon points="41,0 84.5,0 79.5,100 47.5,100" fill="url(#os2)"/>
    <polygon points="84.5,0 85.5,0 80.5,100 79.5,100" fill="#f3e2c8"/>
    <g role="img" aria-label="Tutor and student working together at a desk in front of a bookshelf">
      <polygon points="85.5,0 100,0 100,100 80.5,100" fill="url(#ps2)"/>
    </g>
  </svg>
  <div class="brand">StudyNest<span class="dot"></span></div>
  <div class="divider"></div>
  <div class="offer"><span class="ratio">1:1 IN-HOME</span><span class="kind">TUTORING</span></div>
  <div class="headline">The Best Tutor For Your Child</div>
  <div class="cta">Free Assessment - Find Out More</div>
</div>

<div class="banner strip" style="left:141px;top:836px;width:919px;height:114px;font-size:114px">
  <svg class="art" viewBox="0 0 100 100" preserveAspectRatio="none">
    <defs>
      <linearGradient id="gs3" x1="0" y1="0" x2="1" y2="0"><stop offset="0" stop-color="#e4e4e4"/><stop offset=".5" stop-color="#fff"/><stop offset="1" stop-color="#e8e8e8"/></linearGradient>
      <linearGradient id="os3" x1="0" y1="0" x2="0" y2="1"><stop offset="0" stop-color="#f9a24d"/><stop offset="1" stop-color="#f37a30"/></linearGradient>
      <linearGradient id="ps3" x1="0" y1="0" x2="1" y2="1"><stop offset="0" stop-color="var(--photo-a)"/><stop offset="1" stop-color="var(--photo-b)"/></linearGradient>
    </defs>
    <rect width="100" height="100" fill="url(#gs3)"/>
    <path d="M0,0 L6,0 C2.5,25 1,60 1,100 L0,100Z" fill="var(--blue)"/>
    <polygon points="38.8,0 40.8,0 47.2,100 45.2,100" fill="var(--steel)"/>
    <polygon points="40.8,0 83.5,0 78.5,100 47.2,100" fill="url(#os3)"/>
    <polygon points="83.5,0 84.5,0 79.5,100 78.5,100" fill="#f3e2c8"/>
    <g role="img" aria-label="Tutor and student working together at a desk in front of a bookshelf">
      <polygon points="84.5,0 100,0 100,100 79.5,100" fill="url(#ps3)"/>
    </g>
  </svg>
  <div class="brand">StudyNest<span class="dot"></span></div>
  <div class="divider"></div>
  <div class="offer"><span class="ratio">1:1 IN-HOME</span><span class="kind">TUTORING</span></div>
  <div class="headline">The Best Tutor For Your Child</div>
  <div class="cta">Free Assessment - Find Out More</div>
</div>

</body>
</html>
```